Business Card for a Wedding Films Business

We require a business card design for our business 'Lewis Marrow Wedding Films'. The logo needs to look classy and high end.

Target Market(s)

Wedding Couples

Contact Information for Business Card

Lewis Marrow Wedding Films
07312 605 227
films@lewismarrowreels.com
www.lewismarrowreels.com

Facebook: @lewismarrowweddingfilms
Instagram: @lewismarrowfilms

Font styles to use
Sans Serif

Requirements
Must have
• Social media icons - Facebook and Instagram

```html
<!DOCTYPE html>
<html lang="en">
<head>
<meta charset="utf-8">
<title>Lewis Marrow Wedding Films – Business Card</title>
<link href="https://fonts.googleapis.com/css2?family=Lato:wght@300;400&family=Montserrat:wght@600&display=swap" rel="stylesheet">
<style>
  :root {
    --backdrop: #d9d9d9;
    --card-white: #f7f7f7;
    --card-black: #1a1a1a;
    --ink: #1c1c1c;
    --ink-soft: #3a3a3a;
    --gold: #a88d54;
    --white: #ffffff;
  }
  * { margin: 0; padding: 0; box-sizing: border-box; }
  html, body {
    width: 1200px; height: 884px; overflow: hidden;
    background: var(--backdrop);
  }
  .canvas {
    position: relative; width: 1200px; height: 884px;
    display: flex; align-items: center; justify-content: center; gap: 40px;
  }
  .card {
    position: relative; width: 540px; height: 309px;
    box-shadow: 0 6px 18px rgba(0,0,0,0.18);
  }
  .card--front { background: var(--card-black); }
  .card--back { background: var(--card-white); }

  .brand-name {
    font-family: "Montserrat", sans-serif; font-weight: 600;
    text-transform: uppercase; line-height: 1.35;
  }
  .brand-name .line-main { display: block; font-size: 22px; letter-spacing: 7px; }
  .brand-name .line-sub { display: block; font-size: 11px; letter-spacing: 7px; }

  .card--front .brand {
    position: absolute; left: 0; right: 0; top: 50%; transform: translateY(-50%);
    display: flex; flex-direction: column; align-items: center; gap: 18px;
  }
  .card--front .brand-name { color: var(--white); text-align: center; }
  .brand-mark { width: 18px; height: 18px; background: var(--gold); }

  .card--back .brand {
    position: absolute; right: 40px; top: 150px;
    display: flex; align-items: center; gap: 12px;
  }
  .card--back .brand-name { color: var(--ink); }
  .card--back .brand-name .line-main { font-size: 15px; letter-spacing: 5px; }
  .card--back .brand-name .line-sub { font-size: 8px; letter-spacing: 5px; }
  .card--back .brand-mark { width: 13px; height: 13px; }

  .contact {
    position: absolute; left: 26px; bottom: 26px;
    font-family: "Lato", sans-serif; font-weight: 300;
    font-size: 12.5px; color: var(--ink-soft);
    display: grid; grid-template-columns: auto auto; column-gap: 14px; row-gap: 5px;
  }
  .contact-item { display: flex; align-items: center; gap: 6px; white-space: nowrap; }
  .icon {
    width: 12px; height: 12px; flex: none;
    background: var(--gold); border-radius: 2px;
    display: flex; align-items: center; justify-content: center;
  }
  .icon svg { width: 9px; height: 9px; }
  .icon--round { border-radius: 50%; }
</style>
</head>
<body>
<main class="canvas">

  <section class="card card--front" aria-label="Card front">
    <div class="brand">
      <span class="brand-mark"></span>
      <p class="brand-name">
        <span class="line-main">Lewis Marrow</span>
        <span class="line-sub">Wedding Films</span>
      </p>
    </div>
  </section>

  <section class="card card--back" aria-label="Card back">
    <div class="brand">
      <span class="brand-mark"></span>
      <p class="brand-name">
        <span class="line-main">Lewis Marrow</span>
        <span class="line-sub">Wedding Films</span>
      </p>
    </div>

    <ul class="contact" style="list-style:none">
      <li class="contact-item" style="grid-column:1 / span 2">
        <span class="icon">
          <svg viewBox="0 0 10 10"><path d="M2 1 L4 1 L4.6 3 L3.4 3.8 Q4.5 6 6.2 6.6 L7 5.4 L9 6 L9 8 Q9 9 8 9 Q1 8.5 1 2 Q1 1 2 1 Z" fill="#fff"/></svg>
        </span>07312 605 227
      </li>
      <li class="contact-item">
        <span class="icon">
          <svg viewBox="0 0 10 10"><rect x="1" y="2.5" width="8" height="5.5" fill="none" stroke="#fff" stroke-width="1"/><path d="M1 2.5 L5 5.8 L9 2.5" fill="none" stroke="#fff" stroke-width="1"/></svg>
        </span>films@lewismarrowreels.com
      </li>
      <li class="contact-item">
        <span class="icon icon--round">
          <svg viewBox="0 0 10 10"><circle cx="5" cy="5" r="3.8" fill="none" stroke="#fff" stroke-width="0.9"/><path d="M1.2 5 H8.8 M5 1.2 Q2.8 5 5 8.8 M5 1.2 Q7.2 5 5 8.8" fill="none" stroke="#fff" stroke-width="0.8"/></svg>
        </span>www.lewismarrowreels.com
      </li>
      <li class="contact-item">
        <span class="icon"></span>@lewismarrowweddingfilms
      </li>
      <li class="contact-item">
        <span class="icon"></span>@lewismarrowfilms
      </li>
    </ul>
  </section>

</main>
</body>
</html>
```